BrookhavenLLC

Real Estate Investment. Buy/Sell house/investment . Trustworthy,Reliable, and friendly

Industry/Entity Type

Real Estate

Contact Information for Business Card

Brookhaven@mailbox-example.com
808-555-0143
Linnea-Joy Patterson

```html
<!DOCTYPE html>
<html lang="en">
<head>
<meta charset="utf-8">
<title>Brookhaven LLC – Business Card</title>
<link href="https://fonts.googleapis.com/css2?family=Cinzel:wght@500&family=Arimo:wght@400&display=swap" rel="stylesheet">
<style>
  :root {
    --page-bg: #e9e6e1;
    --card-white: #ffffff;
    --ink: #111111;
    --band-black: #050505;
    --rule-grey: #9a97a0;
    --photo-warm: #e7c27a;
    --photo-skin: #f1c9ae;
    --photo-roof: #6d7078;
  }
  * { margin: 0; padding: 0; box-sizing: border-box; }
  html, body { width: 1200px; height: 800px; overflow: hidden; }
  body {
    background: var(--page-bg);
    display: flex;
    align-items: center;
    justify-content: center;
    font-family: "Arimo", Arial, sans-serif;
  }
  .business-card {
    position: relative;
    width: 1000px;
    height: 572px;
    background: var(--card-white);
    overflow: hidden;
    box-shadow: 0 6px 24px rgba(0,0,0,0.18);
  }
  .hero-photo {
    position: absolute;
    left: 40px;
    top: 40px;
    width: 270px;
    height: 220px;
    border-radius: 6px;
    background: radial-gradient(ellipse at 55% 40%, var(--photo-warm) 0%, var(--photo-roof) 38%, var(--photo-skin) 62%, var(--card-white) 88%);
  }
  .brand-block {
    position: absolute;
    right: 40px;
    top: 60px;
    text-align: right;
    color: var(--ink);
  }
  .brand-name {
    font-family: "Cinzel", "Times New Roman", serif;
    font-weight: 500;
    font-size: 46px;
    letter-spacing: 1px;
    line-height: 1;
  }
  .brand-tagline {
    font-size: 24px;
    line-height: 1.15;
    margin-top: 12px;
  }
  .contact-name {
    position: absolute;
    right: 40px;
    top: 270px;
    text-align: right;
    font-size: 30px;
    line-height: 1.05;
    color: var(--ink);
  }
  .phone-band {
    position: absolute;
    left: 0;
    top: 300px;
    width: 460px;
    height: 220px;
    background: var(--band-black);
  }
  .phone-line {
    position: absolute;
    left: 48px;
    top: 44px;
    display: flex;
    align-items: center;
    gap: 22px;
    color: var(--card-white);
    font-size: 28px;
    letter-spacing: 1px;
  }
  .phone-line svg { width: 20px; height: 24px; fill: var(--card-white); }
  .email-panel-rule {
    position: absolute;
    left: 460px;
    right: 0;
    top: 370px;
    height: 4px;
    background: var(--rule-grey);
  }
  .email-line {
    position: absolute;
    right: 40px;
    top: 420px;
    display: flex;
    align-items: center;
    gap: 20px;
    font-size: 24px;
    color: var(--ink);
    white-space: nowrap;
  }
  .email-line svg { width: 24px; height: 18px; fill: var(--ink); }
  .footer-stripe {
    position: absolute;
    left: 460px;
    right: 0;
    top: 500px;
    height: 20px;
    background: var(--band-black);
  }
</style>
</head>
<body>
  <div class="business-card">
    <div class="hero-photo" role="img" aria-label="Photo of a hand holding a small model house with a set of keys"></div>

    <div class="brand-block">
      <div class="brand-name">Brookhaven LLC</div>
      <div class="brand-tagline">Real Estate Investment<br>Buy/Sell house/investment</div>
    </div>

    <div class="contact-name">Linnea-Joy<br>Patterson</div>

    <div class="phone-band">
      <div class="phone-line">
        <svg viewBox="0 0 20 24" aria-hidden="true"><path d="M4 1c1 0 2 0 2.6 1.2l1.6 3.6c.4 1-.2 1.8-1 2.3l-1.4.9c.8 3 2.6 5.8 5 7.6l1.3-1c.8-.6 1.8-.7 2.5 0l2.6 2.8c.7.8.5 2-.3 2.7l-1.7 1.4c-1.4 1.1-3.4 1-5-.2C5 19 1.6 13 1 6.5 .8 4.3 1.6 2.2 3.2 1.3 3.5 1.1 3.7 1 4 1z"/></svg>
        <span>808-555-0143</span>
      </div>
    </div>

    <div class="email-panel-rule"></div>
    <div class="email-line">
      <span>Brookhaven@mailbox-example.com</span>
      <svg viewBox="0 0 24 18" aria-hidden="true"><path d="M0 0h24v18H0z M2 2l10 8 10-8v-.1H2z" fill-rule="evenodd"/></svg>
    </div>
    <div class="footer-stripe"></div>
  </div>
</body>
</html>
```